Varnek Group Business Card

Varnek Group — Business Card Design Brief
Overview
Design a double-sided business card for Varnek Group that highlights our two service arms: Varnek Communications (telecommunications) and Varnek Energy (business energy solutions). The card should feel smart and stand out when handed to clients.

Objectives
Showcase our areas of specialty clearly.
Reflect the overall Varnek / Varnek Group brand while acknowledging both arms.
Explore using both logos (Communications + Energy) or one unified logo, depending on the design.

Deliverables
One double-sided business card design (front + back).

Content & Copy
Front (preferred): Logo: Varnek / Varnek Group
Descriptor: Business Communications | Business Energy
Back:My contact details and company details
Core products: Business Mobile • Telephony • Internet • Business Energy Solutions

Brand & Visual Direction
We have a group logo currently tailored more toward telecoms, plus a separate Varnek Energy logo.
Please explore layouts that use both logos or just one, whichever works best.
Color: I wouldn't mind seeing an option using our the Blue/Purple gradient from our website (varnek-example.co.uk), but also open to non-gradient approaches and other colours..

Overall look: Smart, modern, and distinctive.
Format & Print Specs
Double-sided business card format. (Use a standard size

Must-Haves
Front: Varnek wording or Varnek Group wording with atleast 1 logo also on front “Business Communications | Business Energy.”

Back: Contact + company details and core products.
A design that stands out while remaining professional.

Nice-to-Have Options
A gradient version using our site’s Blue/Purple gradient.
A non-gradient version.
A dual-logo treatment versus a single-logo treatment.

Thanks
Dominic

```html
<!DOCTYPE html>
<html lang="en">
<head>
<meta charset="utf-8">
<title>Varnek Group — Business Card Backs</title>
<link rel="stylesheet" href="https://fonts.googleapis.com/css2?family=Lato:wght@400;700;900&display=swap">
<style>
  :root {
    --sheet-bg: #ffffff;
    --ink: #111111;
    --card-navy: #1d1862;
    --card-magenta: #9a0cc4;
    --card-blue: #2258c8;
    --arc-purple: #8a20c8;
    --soft-blue: #2b3dd2;
    --mark-blue: #1a62e0;
    --name-silver: #a9acb6;
    --name-white: #ffffff;
    --tagline: #ffffff;
  }
  * { box-sizing: border-box; margin: 0; padding: 0; }
  html, body { width: 913px; height: 1200px; overflow: hidden; background: var(--sheet-bg); }
  body { position: relative; font-family: "Lato", sans-serif; }

  .card {
    position: absolute;
    width: 320px;
    height: 183px;
    border-radius: 10px;
    overflow: hidden;
    background:
      radial-gradient(ellipse 70% 80% at 0% 0%, var(--card-magenta) 0%, rgba(154,12,196,0) 60%),
      radial-gradient(ellipse 60% 70% at 100% 100%, var(--card-blue) 0%, rgba(34,88,200,0) 70%),
      var(--card-navy);
  }
  .card .decor { position: absolute; inset: 0; width: 100%; height: 100%; }

  .brand-mark {
    position: absolute;
    left: 92px; top: 33px;
    width: 70px; height: 70px;
    border-radius: 50%;
    background: var(--mark-blue);
  }
  .brand-name {
    position: absolute;
    left: 0; right: 0;
    top: 108px;
    text-align: center;
    font-weight: 900;
    font-size: 33px;
    line-height: 1;
    letter-spacing: 0.5px;
  }
  .brand-name--silver { color: var(--name-silver); }
  .brand-name--white { color: var(--name-white); }

  .tagline {
    position: absolute;
    left: 0; right: 0;
    text-align: center;
    color: var(--tagline);
    line-height: 1;
  }
  .tagline--business { top: 164px; font-size: 6.2px; font-weight: 400; letter-spacing: 0.4px; }
  .tagline--business strong { font-weight: 900; }
  .tagline--spaced { top: 164px; font-size: 6.2px; font-weight: 700; letter-spacing: 3px; }
  .tagline--tight { top: 142px; font-size: 6.2px; font-weight: 700; letter-spacing: 2.3px; }

  .label {
    position: absolute;
    width: 200px;
    text-align: center;
    font-weight: 900;
    font-size: 11px;
    color: var(--ink);
    letter-spacing: 0.2px;
  }
</style>
</head>
<body>

<!-- Column 1 -->
<div class="card" style="left:115px; top:166px;">
  <svg class="decor" viewBox="0 0 320 183" aria-hidden="true">
    <circle cx="43" cy="139" r="103" fill="none" stroke="var(--arc-purple)" stroke-width="11" opacity=".45"/>
    <circle cx="43" cy="139" r="75" fill="none" stroke="var(--arc-purple)" stroke-width="6" opacity=".35"/>
    <circle cx="190" cy="139" r="43" fill="none" stroke="var(--soft-blue)" stroke-width="8" opacity=".35"/>
    <circle cx="277" cy="139" r="43" fill="var(--soft-blue)" opacity=".5"/>
  </svg>
  <div class="brand-mark"></div>
  <div class="brand-name brand-name--silver">VARNEK</div>
  <p class="tagline tagline--business">BUSINESS <strong>COMMUNICATIONS</strong> + BUSINESS <strong>ENERGY</strong></p>
</div>
<div class="label" style="left:183px; top:364px;">BACK 01</div>

<div class="card" style="left:115px; top:392px;">
  <svg class="decor" viewBox="0 0 320 183" aria-hidden="true">
    <circle cx="43" cy="139" r="103" fill="none" stroke="var(--arc-purple)" stroke-width="11" opacity=".45"/>
    <circle cx="43" cy="139" r="75" fill="none" stroke="var(--arc-purple)" stroke-width="6" opacity=".35"/>
    <circle cx="190" cy="139" r="43" fill="none" stroke="var(--soft-blue)" stroke-width="8" opacity=".35"/>
    <circle cx="277" cy="139" r="43" fill="var(--soft-blue)" opacity=".5"/>
  </svg>
  <div class="brand-mark"></div>
  <div class="brand-name brand-name--silver">VARNEK</div>
  <p class="tagline tagline--spaced">COMMUNICATIONS + ENERGY</p>
</div>
<div class="label" style="left:183px; top:590px;">BACK 02</div>

<div class="card" style="left:115px; top:618px;">
  <svg class="decor" viewBox="0 0 320 183" aria-hidden="true">
    <circle cx="43" cy="139" r="103" fill="none" stroke="var(--arc-purple)" stroke-width="11" opacity=".45"/>
    <circle cx="43" cy="139" r="75" fill="none" stroke="var(--arc-purple)" stroke-width="6" opacity=".35"/>
    <circle cx="190" cy="139" r="43" fill="none" stroke="var(--soft-blue)" stroke-width="8" opacity=".35"/>
    <circle cx="277" cy="139" r="43" fill="var(--soft-blue)" opacity=".5"/>
  </svg>
  <div class="brand-mark"></div>
  <div class="brand-name brand-name--silver">VARNEK</div>
  <p class="tagline tagline--tight">COMMUNICATIONS + ENERGY</p>
</div>
<div class="label" style="left:183px; top:816px;">BACK 03</div>

<div class="card" style="left:115px; top:844px;">
  <svg class="decor" viewBox="0 0 320 183" aria-hidden="true">
    <circle cx="274" cy="91" r="87" fill="none" stroke="var(--arc-purple)" stroke-width="10" opacity=".5"/>
    <circle cx="274" cy="91" r="68" fill="none" stroke="var(--arc-purple)" stroke-width="4" opacity=".45"/>
  </svg>
  <div class="brand-mark"></div>
  <div class="brand-name brand-name--silver">VARNEK</div>
  <p class="tagline tagline--spaced">COMMUNICATIONS + ENERGY</p>
</div>
<div class="label" style="left:183px; top:1051px;">BACK 04</div>

<!-- Column 2 -->
<div class="card" style="left:479px; top:166px;">
  <svg class="decor" viewBox="0 0 320 183" aria-hidden="true">
    <circle cx="43" cy="139" r="103" fill="none" stroke="var(--arc-purple)" stroke-width="11" opacity=".6"/>
    <circle cx="43" cy="139" r="75" fill="none" stroke="var(--arc-purple)" stroke-width="6" opacity=".45"/>
    <circle cx="190" cy="139" r="43" fill="none" stroke="var(--soft-blue)" stroke-width="8" opacity=".45"/>
    <circle cx="277" cy="139" r="43" fill="var(--soft-blue)" opacity=".7"/>
  </svg>
  <div class="brand-mark"></div>
  <div class="brand-name brand-name--white">VARNEK</div>
  <p class="tagline tagline--business">BUSINESS <strong>COMMUNICATIONS</strong> + BUSINESS <strong>ENERGY</strong></p>
</div>
<div class="label" style="left:539px; top:360px;">BACK 05</div>

<div class="card" style="left:479px; top:392px;">
  <svg class="decor" viewBox="0 0 320 183" aria-hidden="true">
    <circle cx="43" cy="139" r="103" fill="none" stroke="var(--arc-purple)" stroke-width="11" opacity=".6"/>
    <circle cx="43" cy="139" r="75" fill="none" stroke="var(--arc-purple)" stroke-width="6" opacity=".45"/>
    <circle cx="190" cy="139" r="43" fill="none" stroke="var(--soft-blue)" stroke-width="8" opacity=".45"/>
    <circle cx="277" cy="139" r="43" fill="var(--soft-blue)" opacity=".7"/>
  </svg>
  <div class="brand-mark"></div>
  <div class="brand-name brand-name--white">VARNEK</div>
  <p class="tagline tagline--spaced">COMMUNICATIONS + ENERGY</p>
</div>
<div class="label" style="left:539px; top:590px;">BACK 06</div>

<div class="card" style="left:479px; top:620px;">
  <svg class="decor" viewBox="0 0 320 183" aria-hidden="true">
    <circle cx="43" cy="139" r="103" fill="none" stroke="var(--arc-purple)" stroke-width="11" opacity=".6"/>
    <circle cx="43" cy="139" r="75" fill="none" stroke="var(--arc-purple)" stroke-width="6" opacity=".45"/>
    <circle cx="190" cy="139" r="43" fill="none" stroke="var(--soft-blue)" stroke-width="8" opacity=".45"/>
    <circle cx="277" cy="139" r="43" fill="var(--soft-blue)" opacity=".7"/>
  </svg>
  <div class="brand-mark"></div>
  <div class="brand-name brand-name--white">VARNEK</div>
  <p class="tagline tagline--tight">COMMUNICATIONS + ENERGY</p>
</div>
<div class="label" style="left:539px; top:816px;">BACK 07</div>

<div class="card" style="left:479px; top:844px;">
  <svg class="decor" viewBox="0 0 320 183" aria-hidden="true">
    <circle cx="274" cy="91" r="87" fill="none" stroke="var(--arc-purple)" stroke-width="10" opacity=".55"/>
    <circle cx="274" cy="91" r="68" fill="none" stroke="var(--arc-purple)" stroke-width="4" opacity=".5"/>
  </svg>
  <div class="brand-mark"></div>
  <div class="brand-name brand-name--white">VARNEK</div>
  <p class="tagline tagline--spaced">COMMUNICATIONS + ENERGY</p>
</div>
<div class="label" style="left:539px; top:1051px;">BACK 08</div>

</body>
</html>
```